Bubble solution bottle label for children

I would like a design for a label for a new bubble solution we have created. We'd like it to appeal to parents as well as 5-10 year old kids. It needs to be whimsical and attractive. The name of the bubbles is:

Twirly Fizz!

We also need a portion of the label to include the following warning:
"Do not drink bubble solution. If swallowed drink lots of water. Bubble solution is not intended for human or animal consumption. If it comes in contact with your eyes, rinse immediately with water"

The label is full bleed and needs to meet the criteria below:
Horizontal
3.54" x 2.05"
90 x 52 mm
1063 x 615 pixels

Target Market(s)

5-10 years old children and their parents

Font styles to use
Serif
Script

Requirements
Must have
• Warning label as written in description. Must be whimsical and attractive for a parent to purchase for their child

```html
<!DOCTYPE html>
<html lang="en">
<head>
<meta charset="utf-8">
<title>Twirly Fizz! – Bubble Solution Label</title>
<link rel="stylesheet" href="https://fonts.googleapis.com/css2?family=Passion+One:wght@900&family=Righteous&family=Oswald:wght@400;600&display=swap">
<style>
  :root {
    --ink: #0b0b0b;
    --lavender: #c9b8f5;
    --violet: #9a86ee;
    --sky: #b9d6f7;
    --mist: #f6f3ff;
    --meadow: #2f9a0c;
  }
  html, body {
    margin: 0;
    padding: 0;
    overflow: hidden;
    background: #ffffff;
  }
  .label {
    position: relative;
    width: 1200px;
    height: 695px;
    overflow: hidden;
  }
  .label__backdrop {
    position: absolute;
    inset: 0;
    background:
      radial-gradient(ellipse at 30% 45%, var(--violet) 0%, rgba(154,134,238,0) 55%),
      radial-gradient(ellipse at 75% 55%, var(--lavender) 0%, rgba(201,184,245,0) 60%),
      radial-gradient(ellipse at 50% 15%, var(--mist) 0%, rgba(246,243,255,0) 45%),
      linear-gradient(135deg, var(--sky) 0%, var(--mist) 35%, var(--lavender) 65%, var(--sky) 100%);
  }
  .label__art {
    position: absolute;
    inset: 0;
  }
  .product-name {
    font-family: "Passion One", "Arial Black", sans-serif;
    font-weight: 900;
    fill: var(--ink);
  }
  .tagline {
    font-family: "Righteous", "Arial Black", sans-serif;
    font-size: 118px;
    fill: var(--meadow);
  }
  .warning {
    font-family: "Oswald", "Arial Narrow", sans-serif;
    font-weight: 400;
    font-size: 24px;
    fill: var(--ink);
  }
  .warning__lead {
    font-weight: 600;
    font-size: 26px;
  }
  .warning__maker {
    font-size: 22px;
  }
</style>
</head>
<body>
  <main class="label">
    <div class="label__backdrop" role="img" aria-label="Soft field of translucent blue and lavender soap bubbles"></div>

    <svg class="label__art" width="1200" height="695" viewBox="0 0 1200 695">
      <text class="product-name" x="42" y="248" font-size="215" textLength="1118" lengthAdjust="spacingAndGlyphs">Twirly Fizz!</text>

      <text class="tagline" x="112" y="466" textLength="976" lengthAdjust="spacingAndGlyphs">Pop! Float! Play!</text>

      <g class="warning" text-anchor="middle">
        <text x="869" y="530" textLength="372" lengthAdjust="spacingAndGlyphs"><tspan class="warning__lead">warning:</tspan>"Do not drink bubble solution.</text>
        <text x="869" y="570" textLength="297" lengthAdjust="spacingAndGlyphs">If swallowed drink lots of water.</text>
        <text x="870" y="607" textLength="600" lengthAdjust="spacingAndGlyphs">Bubble solution is not intended for human or animal consumption.</text>
        <text x="870" y="644" textLength="625" lengthAdjust="spacingAndGlyphs">If it comes in contact with your eyes, rinse immediately with water"</text>
        <text class="warning__maker" x="870" y="681" textLength="170" lengthAdjust="spacingAndGlyphs">BRIGHT DAYS LLC</text>
      </g>
    </svg>
  </main>
</body>
</html>
```